Podiatry clinic requires a modern revamp and editing of existing website.

I would like a fresh new look and updated information for my current business website. An easy to navigate site with prominent address and phone number for call to action. We are a podiatry clinic that focuses on general and sports podiatry.
I would like 4 pages; including Home page, About Us, Services & Contact.
www.brambleridgefootcare.com

Target Market(s)

Active working professionals.

Industry/Entity Type

Medical

Coding

Coded - Design and coding required

Number of Pages Required

4 page

Font styles to use
Sans Serif

Colors
6b449b

Requirements
Must have
• A modern look with logo and active images; clean and uncluttered. Visible phone number and address for call to action.
• 4 pages - Home, About Us, Services, Contact.
• Home page - update address & service logos.
• About Us - update of personal information.
• Services - Revamp of existing page.
• Contact page to include Google map, email & phone number.
Nice to have
• Ability to add content easily; eg. a blog or adding video onto Home page.
• Link to Friendspace page.

```html
<!DOCTYPE html>
<html lang="en">
<head>
<meta charset="utf-8">
<title>Bramble Ridge Foot Care</title>
<link rel="stylesheet" href="https://fonts.googleapis.com/css2?family=Open+Sans:wght@400;600;700&family=Raleway:wght@300;400;500;600;700;800&display=swap">
<style>
:root{
  --purple:#47308e;
  --purple-deep:#3e2a86;
  --purple-bar:#5638a6;
  --ink:#555555;
  --ink-dark:#444444;
  --green:#7ab929;
  --grey-band:#efefef;
  --white:#ffffff;
}
html,body{margin:0;padding:0;width:1200px;height:2663px;overflow:hidden;background:var(--white);}
.page{position:relative;width:1200px;height:2663px;overflow:hidden;font-family:"Open Sans",Arial,sans-serif;color:var(--ink);}
a{color:inherit;text-decoration:none;}

/* header */
.site-header{position:absolute;left:0;top:0;width:1200px;height:124px;background:var(--white);z-index:3;}
.brand{position:absolute;left:75px;top:-10px;width:202px;height:202px;border-radius:50%;background:var(--white);z-index:4;display:flex;align-items:center;justify-content:center;gap:10px;}
.brand-dot{width:18px;height:18px;border-radius:50%;background:var(--purple);flex:none;}
.brand-name{font-family:"Raleway",sans-serif;font-weight:700;font-size:25px;line-height:1.05;color:var(--purple);width:120px;}
.main-nav{position:absolute;left:412px;top:44px;font-family:"Raleway",sans-serif;font-size:19px;color:#666;}
.main-nav a{position:absolute;white-space:nowrap;}
.main-nav .active{color:var(--purple);}
.header-phone{position:absolute;left:893px;top:34px;display:flex;align-items:center;gap:15px;}
.phone-badge{width:50px;height:50px;border-radius:50%;background:var(--purple);display:flex;align-items:center;justify-content:center;}
.header-phone .number{font-weight:700;font-size:28px;color:var(--green);white-space:nowrap;}

/* hero */
.hero{position:absolute;left:0;top:124px;width:1200px;height:574px;}
.hero-photo{position:absolute;inset:0;background:
  radial-gradient(ellipse at 78% 45%, #f3c766 0%, #e0a444 25%, transparent 55%),
  linear-gradient(180deg,#d9a552 0%,#c78a3c 40%,#7a6a58 62%,#4b4742 100%);}
.hero-title{position:absolute;left:78px;top:255px;margin:0;font-family:"Raleway",sans-serif;font-weight:800;font-size:46px;line-height:76px;color:var(--purple);text-transform:uppercase;white-space:nowrap;}
.hero-sub{position:absolute;left:80px;top:402px;margin:0;font-size:21px;line-height:31px;color:var(--purple);width:380px;}
.hero-btn{position:absolute;left:78px;top:522px;width:227px;height:59px;border-radius:30px;background:var(--purple);color:var(--white);font-family:"Raleway",sans-serif;font-size:25px;font-weight:500;display:flex;align-items:center;justify-content:center;}

/* enquiry band */
.enquiry-band{position:absolute;left:0;top:698px;width:1200px;height:134px;background:var(--purple);color:var(--white);font-family:"Raleway",sans-serif;}
.enquiry-band .lead{position:absolute;left:80px;top:48px;font-size:34px;font-weight:400;white-space:nowrap;}
.enquiry-band .call{position:absolute;left:604px;top:22px;display:flex;align-items:center;gap:12px;font-size:32px;white-space:nowrap;}
.call .ring{width:50px;height:50px;border-radius:50%;border:2px solid var(--white);display:flex;align-items:center;justify-content:center;box-sizing:border-box;}
.call .number{font-family:"Open Sans",sans-serif;font-weight:700;font-size:32px;}
.enquiry-band .mail{position:absolute;left:604px;top:84px;font-family:"Open Sans",sans-serif;font-size:21px;display:flex;align-items:center;gap:8px;white-space:nowrap;}

/* treatments */
.treatment{position:absolute;top:864px;width:540px;height:200px;}
.treatment .thumb{position:absolute;left:0;top:0;width:181px;height:181px;border-radius:50%;border:1px solid #ddd;box-sizing:border-box;}
.treatment h3{position:absolute;left:204px;top:14px;margin:0;font-family:"Raleway",sans-serif;font-weight:500;font-size:28px;line-height:36px;color:var(--purple);white-space:nowrap;}
.treatment p{position:absolute;left:204px;top:64px;margin:0;width:292px;font-size:14.5px;line-height:26px;color:var(--ink);}
.read-more{position:absolute;left:204px;top:152px;font-family:"Raleway",sans-serif;font-weight:700;font-size:16px;color:var(--purple);display:flex;align-items:center;gap:6px;white-space:nowrap;}

/* welcome */
.welcome{position:absolute;left:0;top:1092px;width:1200px;height:218px;background:var(--grey-band);text-align:center;}
.section-title{margin:0;font-family:"Raleway",sans-serif;font-weight:300;font-size:42px;color:#555;text-transform:uppercase;white-space:nowrap;}
.section-title strong{font-weight:400;color:var(--purple);}
.welcome .section-title{position:absolute;left:0;right:0;top:44px;}
.welcome p{position:absolute;left:205px;width:790px;top:116px;margin:0;font-size:14.5px;line-height:25px;color:var(--ink);}

/* news */
.news .section-title{position:absolute;left:0;right:0;top:1358px;text-align:center;}
.news-card{position:absolute;top:1424px;width:234px;}
.news-card .photo{width:234px;height:145px;border:1px solid #ddd;box-sizing:border-box;}
.news-card h4{margin:12px 0 0;font-weight:400;font-size:17px;line-height:25px;color:var(--purple);}
.news-card .date{margin-top:6px;font-size:14px;color:#888;display:flex;align-items:center;gap:6px;}
.news-card p{margin:6px 0 0;font-size:15px;line-height:25px;color:var(--ink);}

/* about */
.about{position:absolute;left:0;top:1816px;width:1200px;height:364px;background:var(--grey-band);}
.video{position:absolute;left:78px;top:60px;width:431px;height:240px;background:linear-gradient(135deg,#8f8f8f,#c9c9c9 55%,#a8a8a8);display:flex;align-items:center;justify-content:center;}
.about .section-title{position:absolute;left:547px;top:50px;}
.about p{position:absolute;left:547px;width:570px;margin:0;font-size:15px;line-height:25px;color:var(--ink);}

/* partners */
.partner{position:absolute;top:2237px;height:70px;border-radius:8px;}

/* footer */
.site-footer{position:absolute;left:0;top:2356px;width:1200px;height:254px;background:var(--purple);color:var(--white);}
.footer-brand{position:absolute;left:80px;top:50px;display:flex;align-items:center;gap:10px;}
.footer-brand .dot{width:18px;height:18px;border-radius:50%;background:#b7a9d8;}
.footer-brand .name{font-family:"Raleway",sans-serif;font-weight:700;font-size:28px;line-height:1.1;color:#b7a9d8;width:190px;}
.footer-col{position:absolute;top:38px;}
.footer-col h5{margin:0 0 18px;font-family:"Raleway",sans-serif;font-weight:400;font-size:22px;white-space:nowrap;}
.footer-col ul{list-style:none;margin:0;padding:0;font-size:17px;}
.footer-col li{display:flex;align-items:center;gap:12px;height:37px;}
.contact-list li{align-items:flex-start;height:auto;margin-bottom:14px;font-size:15px;line-height:24px;}
.contact-list li svg{margin-top:4px;flex:none;}
.social li{height:68px;}
.social .disc{width:46px;height:46px;border-radius:50%;background:var(--white);}
.copyright{position:absolute;left:0;top:2610px;width:1200px;height:53px;background:var(--purple-bar);color:var(--white);font-size:15px;display:flex;align-items:center;justify-content:center;}
</style>
</head>
<body>
<div class="page">

  <header class="site-header">
    <nav class="main-nav">
      <a class="active" style="left:0">HOME</a>
      <a style="left:96px">ABOUT</a>
      <a style="left:204px">SERVICES</a>
      <a style="left:335px">CONTACT</a>
    </nav>
    <div class="header-phone">
      <span class="phone-badge">
        <svg width="24" height="24" viewBox="0 0 24 24"><path fill="#fff" d="M6.6 10.8a15.1 15.1 0 0 0 6.6 6.6l2.2-2.2c.3-.3.7-.4 1-.2 1.1.4 2.3.6 3.6.6.6 0 1 .4 1 1V20c0 .6-.4 1-1 1A17 17 0 0 1 3 4c0-.6.4-1 1-1h3.5c.6 0 1 .4 1 1 0 1.3.2 2.5.6 3.6.1.3 0 .7-.2 1z"/></svg>
      </span>
      <span class="number">1300 555 014</span>
    </div>
  </header>
  <div class="brand"><span class="brand-dot"></span><span class="brand-name">Bramble Ridge Foot Care</span></div>

  <section class="hero">
    <div class="hero-photo" role="img" aria-label="Runner's legs in sports shoes on a sunlit road at dusk"></div>
  </section>
  <h1 class="hero-title">Qualified Health<br>Professionals</h1>
  <p class="hero-sub">Various foot conditions, including Sports Injuries, Orthotic Therapy &amp; Nail Surgery</p>
  <a class="hero-btn">CONTACT US</a>

  <section class="enquiry-band">
    <div class="lead">For Appointments or Enquiries</div>
    <div class="call">Please call us on
      <span class="ring"><svg width="22" height="22" viewBox="0 0 24 24"><path fill="#fff" d="M6.6 10.8a15.1 15.1 0 0 0 6.6 6.6l2.2-2.2c.3-.3.7-.4 1-.2 1.1.4 2.3.6 3.6.6.6 0 1 .4 1 1V20c0 .6-.4 1-1 1A17 17 0 0 1 3 4c0-.6.4-1 1-1h3.5c.6 0 1 .4 1 1 0 1.3.2 2.5.6 3.6.1.3 0 .7-.2 1z"/></svg></span>
      <span class="number">1300 555 014</span>
    </div>
    <div class="mail">Email:
      <svg width="20" height="16" viewBox="0 0 20 16"><rect x="1" y="1" width="18" height="14" fill="none" stroke="#fff" stroke-width="2"/><path d="M1 2l9 7 9-7" fill="none" stroke="#fff" stroke-width="2"/></svg>
      info@brambleridgefootcare.com</div>
  </section>

  <article class="treatment" style="left:78px">
    <div class="thumb" role="img" aria-label="Podiatrist examining a patient's foot" style="background:radial-gradient(circle at 50% 50%,#f3ddd0,#d9c2b6 60%,#bfc7cf)"></div>
    <h3>General Treatment</h3>
    <p>Nails, Corns, Callus, Warts, Skin Disorders, Heel pain / Heel Spurs / Arch pain - plantar Fasciitis</p>
    <a class="read-more">READ MORE <svg width="14" height="12" viewBox="0 0 14 12"><path d="M1 1l5 5-5 5M7 1l5 5-5 5" fill="none" stroke="#47308e" stroke-width="2"/></svg></a>
  </article>
  <article class="treatment" style="left:630px">
    <div class="thumb" role="img" aria-label="Gloved hands treating a toenail" style="background:radial-gradient(circle at 50% 55%,#f1d6c6,#e2c3b4 55%,#e9eef2)"></div>
    <h3>Specialised Treatments</h3>
    <p>Diabetic Management, Nail Surgery, Biomechanical Assessment, Gait Analysis, Orthotic Therapy</p>
    <a class="read-more">READ MORE <svg width="14" height="12" viewBox="0 0 14 12"><path d="M1 1l5 5-5 5M7 1l5 5-5 5" fill="none" stroke="#47308e" stroke-width="2"/></svg></a>
  </article>

  <section class="welcome">
    <h2 class="section-title">Welcome to <strong>Bramble Ridge Foot Care</strong></h2>
    <p>Bramble Ridge Foot Care is a Podiatry clinic in the heart of Melbourne CBD. We are located between Hollis &amp; Warren Streets in the Parkline Business Centre / Linden Hotel Complex.</p>
  </section>

  <section class="news">
    <h2 class="section-title">Latest <strong>News</strong></h2>
    <article class="news-card" style="left:78px">
      <div class="photo" role="img" aria-label="Physiotherapist treating a patient's leg in a clinic" style="background:linear-gradient(135deg,#e9e6e2,#c9bfb5 60%,#9d8f84)"></div>
      <h4>Lorem Ipsum is dummy text and simply printing.</h4>
      <div class="date"><svg width="12" height="12" viewBox="0 0 12 12"><rect x="1" y="2" width="10" height="9" fill="none" stroke="#999" stroke-width="1.5"/><path d="M1 5h10" stroke="#999" stroke-width="1.5"/></svg>01 August 2016</div>
      <p>Lorem Ipsum is simply dummy text of the printing and type setting industry.</p>
    </article>
    <article class="news-card" style="left:348px">
      <div class="photo" role="img" aria-label="Bare feet walking along the water's edge" style="background:linear-gradient(180deg,#3f6f8f,#6d93ab 50%,#a8c1cf)"></div>
      <h4>Lorem Ipsum is dummy text and simply printing.</h4>
      <div class="date"><svg width="12" height="12" viewBox="0 0 12 12"><rect x="1" y="2" width="10" height="9" fill="none" stroke="#999" stroke-width="1.5"/><path d="M1 5h10" stroke="#999" stroke-width="1.5"/></svg>01 August 2016</div>
      <p>Lorem Ipsum is simply dummy text of the printing and type setting industry.</p>
    </article>
    <article class="news-card" style="left:619px">
      <div class="photo" role="img" aria-label="Foot showing a highlighted area of heel pain" style="background:radial-gradient(circle at 55% 70%,#e46b6b,#d9b7c0 40%,#f4f4f6 75%)"></div>
      <h4>Lorem Ipsum is dummy text and simply printing.</h4>
      <div class="date"><svg width="12" height="12" viewBox="0 0 12 12"><rect x="1" y="2" width="10" height="9" fill="none" stroke="#999" stroke-width="1.5"/><path d="M1 5h10" stroke="#999" stroke-width="1.5"/></svg>01 August 2016</div>
      <p>Lorem Ipsum is simply dummy text of the printing and type setting industry.</p>
    </article>
    <article class="news-card" style="left:889px">
      <div class="photo" role="img" aria-label="Clinician consulting with a patient" style="background:linear-gradient(135deg,#f6f1ee,#e8b9c4 55%,#c9a7a0)"></div>
      <h4>Lorem Ipsum is dummy text and simply printing.</h4>
      <div class="date"><svg width="12" height="12" viewBox="0 0 12 12"><rect x="1" y="2" width="10" height="9" fill="none" stroke="#999" stroke-width="1.5"/><path d="M1 5h10" stroke="#999" stroke-width="1.5"/></svg>01 August 2016</div>
      <p>Lorem Ipsum is simply dummy text of the printing and type setting industry.</p>
    </article>
  </section>

  <section class="about">
    <div class="video" role="img" aria-label="Video still of a podiatrist trimming a patient's toenail">
      <svg width="60" height="60" viewBox="0 0 60 60"><circle cx="30" cy="30" r="28" fill="rgba(255,255,255,.85)"/><path d="M24 18l18 12-18 12z" fill="#666"/></svg>
    </div>
    <h2 class="section-title">About <strong>Podiatrists</strong></h2>
    <p style="top:126px">Our podiatrists are fully qualified health professionals who are able to diagnose, treat, manage or help to prevent all medical conditions that affect the feet and lower limb.</p>
    <p style="top:225px">We provide General Podiatry Treatment and some Specialised Services in relation to various foot conditions, including Sports Injuries, Orthotic Therapy and Nail Surgery.</p>
  </section>

  <section class="partners" aria-label="Partner and association badges">
    <div class="partner" style="left:89px;width:223px;background:#e4e0ee"></div>
    <div class="partner" style="left:351px;width:240px;background:#e9e9e9"></div>
    <div class="partner" style="left:634px;width:214px;background:#dcebd6"></div>
    <div class="partner" style="left:905px;width:213px;background:#dde6f0"></div>
  </section>

  <footer class="site-footer">
    <div class="footer-brand"><span class="dot"></span><span class="name">Bramble Ridge Foot Care</span></div>
    <div class="footer-col" style="left:350px">
      <h5>Useful Links</h5>
      <ul>
        <li><svg width="16" height="10" viewBox="0 0 16 10"><path d="M0 5h14M10 1l4 4-4 4" fill="none" stroke="#fff" stroke-width="1.6"/></svg>Home</li>
        <li><svg width="16" height="10" viewBox="0 0 16 10"><path d="M0 5h14M10 1l4 4-4 4" fill="none" stroke="#fff" stroke-width="1.6"/></svg>About</li>
        <li><svg width="16" height="10" viewBox="0 0 16 10"><path d="M0 5h14M10 1l4 4-4 4" fill="none" stroke="#fff" stroke-width="1.6"/></svg>Services</li>
        <li><svg width="16" height="10" viewBox="0 0 16 10"><path d="M0 5h14M10 1l4 4-4 4" fill="none" stroke="#fff" stroke-width="1.6"/></svg>Contact</li>
      </ul>
    </div>
    <div class="footer-col" style="left:621px;width:230px">
      <h5>Get In Touch</h5>
      <ul class="contact-list">
        <li><svg width="14" height="18" viewBox="0 0 14 18"><path d="M7 1a6 6 0 0 0-6 6c0 4.5 6 10 6 10s6-5.5 6-10a6 6 0 0 0-6-6z" fill="#fff"/><circle cx="7" cy="7" r="2.2" fill="#47308e"/></svg>Suite 204 / 118 Ridgeway Street Melbourne 3000</li>
        <li style="font-weight:700"><svg width="16" height="16" viewBox="0 0 24 24"><path fill="#fff" d="M6.6 10.8a15.1 15.1 0 0 0 6.6 6.6l2.2-2.2c.3-.3.7-.4 1-.2 1.1.4 2.3.6 3.6.6.6 0 1 .4 1 1V20c0 .6-.4 1-1 1A17 17 0 0 1 3 4c0-.6.4-1 1-1h3.5c.6 0 1 .4 1 1 0 1.3.2 2.5.6 3.6.1.3 0 .7-.2 1z"/></svg>1300 555 014</li>
        <li><svg width="18" height="14" viewBox="0 0 20 16"><rect x="1" y="1" width="18" height="14" fill="none" stroke="#fff" stroke-width="2"/><path d="M1 2l9 7 9-7" fill="none" stroke="#fff" stroke-width="2"/></svg>info@brambleridgefootcare.com</li>
      </ul>
    </div>
    <div class="footer-col" style="left:888px">
      <h5>Follow Us</h5>
      <ul class="social">
        <li><span class="disc"></span>Friendspace</li>
        <li><span class="disc"></span>Chirpline</li>
      </ul>
    </div>
  </footer>
  <div class="copyright">© Bramble Ridge Foot Care- 2016. All Rights Reserved.</div>

</div>
</body>
</html>
```